New Webpage for High Class Expert Witness Services Company

We are looking for a minimalist design for a webpage that just has our logo and an entry form offer to connect with one of our Liaisons.
The entry form should just ask for Name, Email, Contact Info and Description of Project.

Company Name is: The Marlow Crest Advisory Services

Number of Pages Required

1 page

```html
<!DOCTYPE html>
<html lang="en">
<head>
<meta charset="utf-8">
<title>The Marlow Crest Advisory Services — Inquiry for Consultation</title>
<link rel="stylesheet" href="https://fonts.googleapis.com/css2?family=Cinzel:wght@500;600&family=Inter:wght@400;500;600;700&display=swap">
<style>
  :root {
    --bg-deep: #0f0f0f;
    --bg-mid: #1c1c1c;
    --ink-light: #f2f2f2;
    --ink-soft: #cfcfcf;
    --ink-muted: #bdbdbd;
    --card: #ffffff;
    --ink-dark: #141414;
    --field-border: #cfcfcf;
    --placeholder: #777777;
    --rule-dark: #2c2c2c;
    --rule-light: #e4e4e4;
  }
  * { box-sizing: border-box; margin: 0; padding: 0; }
  html, body { width: 1200px; height: 750px; overflow: hidden; }
  body {
    position: relative;
    font-family: "Inter", sans-serif;
    color: var(--ink-light);
    background: var(--bg-deep);
  }
  .backdrop {
    position: absolute; inset: 0;
    background:
      linear-gradient(125deg, transparent 35%, rgba(255,255,255,0.06) 48%, transparent 62%),
      radial-gradient(ellipse at 45% 35%, var(--bg-mid), var(--bg-deep) 75%);
  }
  .brand {
    position: absolute; left: 84px; top: 96px;
    display: flex; align-items: center; gap: 14px;
    font-family: "Cinzel", serif; font-weight: 500;
    font-size: 26px; letter-spacing: 1px; color: var(--ink-soft);
    line-height: 1.15;
  }
  .brand-mark { width: 40px; height: 40px; background: var(--ink-soft); flex: none; }
  .headline {
    position: absolute; left: 84px; top: 230px; width: 400px;
    font-family: "Cinzel", serif; font-weight: 600;
    font-size: 46px; line-height: 45px; letter-spacing: 1px;
    color: var(--ink-light);
  }
  .intro {
    position: absolute; left: 84px; top: 436px; width: 360px;
    padding-left: 25px; border-left: 1px solid var(--ink-muted);
    font-size: 14px; line-height: 24px; color: var(--ink-soft);
  }
  .inquiry-card {
    position: absolute; left: 606px; top: 58px; width: 510px; height: 589px;
    background: var(--card); color: var(--ink-dark);
    padding: 24px 30px 30px;
  }
  .inquiry-title {
    font-family: "Cinzel", serif; font-weight: 600;
    font-size: 29px; line-height: 54px; letter-spacing: 0.3px;
    padding-bottom: 11px; border-bottom: 1px solid var(--rule-light);
    margin-bottom: 18px;
  }
  .field { margin-bottom: 12px; }
  .field-label {
    display: block; font-family: "Cinzel", serif; font-weight: 600;
    font-size: 14px; line-height: 18px; margin-bottom: 9px;
  }
  .field-input {
    display: block; width: 100%; height: 42px;
    border: 1px solid var(--field-border); background: var(--card);
    padding: 0 13px; font-family: "Inter", sans-serif; font-size: 13.5px;
    color: var(--ink-dark);
  }
  .field-input::placeholder { color: var(--placeholder); }
  textarea.field-input { height: 96px; padding-top: 10px; resize: none; }
  .submit-button {
    display: block; width: 100%; height: 48px; margin-top: 12px;
    background: var(--ink-dark); color: #fff; border: 0;
    font-family: "Inter", sans-serif; font-weight: 600;
    font-size: 15px; letter-spacing: 0.5px; text-transform: uppercase;
  }
  .site-footer {
    position: absolute; left: 84px; right: 84px; top: 706px;
    border-top: 1px solid var(--rule-dark);
    display: flex; justify-content: space-between; align-items: center;
    padding-top: 15px; font-size: 11px; color: var(--ink-soft);
  }
  .site-footer strong { font-weight: 600; color: var(--ink-light); }
  .footer-links { display: flex; gap: 12px; align-items: center; }
  .footer-links .sep { width: 1px; height: 9px; background: #444; }
</style>
</head>
<body>
  <div class="backdrop" role="img" aria-label="Dark brushed metal texture background"></div>

  <div class="brand"><span class="brand-mark"></span><span>The Marlow Crest<br>Advisory Services</span></div>

  <h1 class="headline">Unmatched Expertise for Complex Litigation</h1>

  <p class="intro">Secure the specialized insights your case requires. Connect with a member of our elite expert witness team for strategic defense support.</p>

  <form class="inquiry-card">
    <h2 class="inquiry-title">Inquiry for Consultation</h2>
    <div class="field">
      <label class="field-label" for="name">Full Name *</label>
      <input class="field-input" id="name" type="text" placeholder="Your Name Here">
    </div>
    <div class="field">
      <label class="field-label" for="email">Email Address *</label>
      <input class="field-input" id="email" type="email" placeholder="mail@website.com">
    </div>
    <div class="field">
      <label class="field-label" for="phone">Phone Number *</label>
      <input class="field-input" id="phone" type="tel" placeholder="+1 234 567 8900">
    </div>
    <div class="field">
      <label class="field-label" for="project">Description of Project *</label>
      <textarea class="field-input" id="project" placeholder="Describe your project here..."></textarea>
    </div>
    <button class="submit-button" type="button">Connect with an Expert</button>
  </form>

  <footer class="site-footer">
    <span>©2026 &nbsp;<strong>Marlow Crest Advisory Services.</strong> All Rights Reserved.</span>
    <span class="footer-links"><span>Privacy Policy</span><span class="sep"></span><span>Terms &amp; Conditions</span></span>
  </footer>
</body>
</html>
```